Wheel infographic for product offerings

We want an infographic designed that shows our product offerings on a wheel.
Wheel that creates sense of continuous 24/7 monitoring and robust nature of types of risk we are able to sense
At top of wheel, start with BSA-AML Risk:
¬ Process includes:
1. Correlation against PEP, Billionaires, TERN , ABAC and D&E Ecosystems
2. Custom data ecosystem development for enhanced due diligence on specific high-risk entities and individuals
3. Risk ranking based on Ecosystem matches
4. Behavioral Analytics for AML tracking
Next on wheel, point to Physical Security and Critical Infrastructure Risk
¬ Process includes:
1. Correlation against TERN , PLIX, + Qro Ecosystems
2. Custom Data Ecosystem analysis for indications of physical threats
3. Behavioral analytics to optimize Qro findings
Next on wheel point to Compliance and Litigation risk:
Process includes:
1. Correlation against QT/FCA, L&E, D&E, and ABAC Ecosystems
2. Custom data ecosystem targeting relevant class action content
3. QT/FCA Ecosystem intelligence reporting
Next on wheel, point to Reputational Risk
Process includes:
1.Correlation against TERN, L&E, QT/FCA Ecosystems
2. Custom Data Ecosystem for online sentiment monitoring
Next on wheel point to Personnel Risk
Process includes:
1. Correlation of customers, vendors, and employees against all Veradyn ecosystems
2. Company-specific Custom Data Ecosystem Analysis

```html
<!DOCTYPE html>
<html lang="en">
<head>
<meta charset="utf-8">
<title>Veradyn – Risk Monitoring Wheel</title>
<link href="https://fonts.googleapis.com/css2?family=Open+Sans:wght@400;600&display=swap" rel="stylesheet">
<style>
  :root {
    --bg: #ffffff;
    --box: #176e91;
    --lime: #d5e49a;
    --label: #d3e58c;
    --sky: #6cc7ec;
    --steel: #4d91ae;
    --ocean: #6fb6e2;
    --deep: #2f5b6d;
    --ring-top: #4a8fab;
    --white: #ffffff;
  }
  * { box-sizing: border-box; margin: 0; padding: 0; }
  html, body { width: 1132px; height: 1200px; overflow: hidden; background: var(--bg); }
  .canvas { position: relative; width: 1132px; height: 1200px; font-family: "Open Sans", Arial, sans-serif; }
  .wheel { position: absolute; left: 0; top: 0; }
  .wheel-label { fill: var(--label); font-family: "Open Sans", Arial, sans-serif; font-weight: 400; }
  .process-box {
    position: absolute;
    background: var(--box);
    border: 3px solid var(--lime);
    border-radius: 22px;
    color: var(--white);
    font-size: 13.5px;
    line-height: 17.5px;
    padding: 18px 12px 12px 12px;
  }
  .process-box h3 { font-weight: 400; font-size: 13px; text-align: center; margin-bottom: 17px; letter-spacing: 0.2px; }
  .process-box p { margin: 0; }
  .process-box .gap { margin-top: 17px; }
  .box-bsa { left: 456px; top: 74px; width: 280px; height: 262px; }
  .box-physical { left: 826px; top: 298px; width: 278px; height: 218px; }
  .box-physical h3 { text-align: left; padding-left: 10px; margin-bottom: 30px; }
  .box-personnel { left: 58px; top: 383px; width: 277px; height: 177px; }
  .box-personnel h3 { text-align: left; padding-left: 10px; }
  .box-reputational { left: 141px; top: 786px; width: 278px; height: 166px; }
  .box-compliance { left: 747px; top: 808px; width: 277px; height: 198px; }
  .brand { position: absolute; right: 52px; top: 1096px; }
  .brand-name { font-family: "Open Sans", Arial, sans-serif; font-weight: 400; font-size: 60px; color: var(--sky); line-height: 1; }
</style>
</head>
<body>
<div class="canvas">
  <svg class="wheel" width="1132" height="1200" viewBox="0 0 1132 1200">
    <defs>
      <marker id="arrow-head" viewBox="0 0 10 10" refX="5" refY="5" markerWidth="3" markerHeight="3" orient="auto">
        <path d="M0 0 L10 5 L0 10 Z" fill="var(--lime)"/>
      </marker>
    </defs>
    <g fill="none" stroke-width="16">
      <path d="M439.5 394.9 A256 256 0 0 1 740.5 394.9" stroke="var(--ring-top)"/>
      <path d="M740.5 394.9 A256 256 0 0 1 833.5 681.1" stroke="var(--sky)"/>
      <path d="M833.5 681.1 A256 256 0 0 1 590 858" stroke="var(--steel)"/>
      <path d="M590 858 A256 256 0 0 1 346.5 681.1" stroke="var(--deep)"/>
      <path d="M346.5 681.1 A256 256 0 0 1 439.5 394.9" stroke="var(--sky)"/>
    </g>
    <g stroke="var(--lime)" stroke-width="1">
      <path class="slice-bsa" d="M590 602 L444.2 401.4 A248 248 0 0 1 735.8 401.4 Z" fill="var(--sky)"/>
      <path class="slice-physical" d="M590 602 L735.8 401.4 A248 248 0 0 1 825.9 678.6 Z" fill="var(--steel)"/>
      <path class="slice-compliance" d="M590 602 L825.9 678.6 A248 248 0 0 1 590 850 Z" fill="var(--deep)"/>
      <path class="slice-reputational" d="M590 602 L590 850 A248 248 0 0 1 354.1 678.6 Z" fill="var(--ocean)"/>
      <path class="slice-personnel" d="M590 602 L354.1 678.6 A248 248 0 0 1 444.2 401.4 Z" fill="var(--steel)"/>
    </g>
    <g class="hub">
      <circle cx="590" cy="602" r="48" fill="var(--white)"/>
      <g class="cycle-arrows" fill="none" stroke="var(--lime)" stroke-width="5" marker-end="url(#arrow-head)">
        <path d="M590 572 A30 30 0 0 1 615.4 586.1"/>
        <path d="M618.5 592.7 A30 30 0 0 1 613 621.3"/>
        <path d="M607.6 626.3 A30 30 0 0 1 578.8 629.8"/>
        <path d="M572.4 626.3 A30 30 0 0 1 560.1 599.9"/>
        <path d="M561.5 592.7 A30 30 0 0 1 582.7 572.9"/>
      </g>
      <circle cx="590" cy="602" r="15" fill="none" stroke="var(--sky)" stroke-width="2.5" stroke-linecap="round" stroke-dasharray="0.1 5.2"/>
    </g>
    <text class="wheel-label" font-size="19" transform="translate(597 448) rotate(-90)" text-anchor="middle">BSA-AML Risk</text>
    <g class="wheel-label" font-size="15" transform="translate(740 560) rotate(-20)" text-anchor="end">
      <text x="80" y="-28">PHYSICAL SECURITY</text>
      <text x="80" y="-8">AND CRITICAL</text>
      <text x="80" y="12">INFRASTRUCTURE</text>
      <text x="80" y="32">RISK</text>
    </g>
    <g class="wheel-label" font-size="17" transform="translate(684 720) rotate(55)" text-anchor="middle">
      <text x="0" y="-4">Compliance and</text>
      <text x="0" y="16">Litigation risk</text>
    </g>
    <text class="wheel-label" font-size="18" transform="translate(500 712) rotate(-45)" text-anchor="middle">Reputational Risk</text>
    <text class="wheel-label" font-size="22" transform="translate(446 578) rotate(8)" text-anchor="middle">Personnel Risk</text>
    <g fill="var(--lime)">
      <circle cx="590" cy="346" r="18"/>
      <circle cx="826" cy="502" r="18"/>
      <circle cx="746" cy="804" r="18"/>
      <circle cx="417" cy="796" r="18"/>
      <circle cx="342" cy="546" r="18"/>
    </g>
  </svg>

  <div class="process-box box-bsa">
    <h3>PROCESS INCLUDES:</h3>
    <p>1. Correlation against PEP, Billionaires, TERN , ABAC and D&amp;E Ecosystems</p>
    <p>2. Custom data ecosystem development for enhanced due diligence on specific high-risk entities and individuals</p>
    <p>3. Risk ranking based on Ecosystem matches</p>
    <p>4. Behavioral Analytics for AML</p>
  </div>

  <div class="process-box box-physical">
    <h3>PROCESS INCLUDES:</h3>
    <p>1. Correlation against TERN , PLIX, + Qro Ecosystems</p>
    <p>2. Custom Data Ecosystem analysis for indications of physical threats</p>
    <p>3. Behavioral analytics to optimize Qro findings htracking</p>
  </div>

  <div class="process-box box-personnel">
    <h3>PROCESS INCLUDES:</h3>
    <p>1. Correlation of customers, vendors, and employees against all Veradyn ecosystems</p>
    <p class="gap">2. Company-specific Custom Data Ecosystem Analysis</p>
  </div>

  <div class="process-box box-reputational">
    <h3>PROCESS INCLUDES:</h3>
    <p>1.Correlation against TERN, L&amp;E, QT/FCA Ecosystems</p>
    <p class="gap">2. Custom Data Ecosystem for online sentiment monitoring</p>
  </div>

  <div class="process-box box-compliance">
    <h3>PROCESS INCLUDES:</h3>
    <p>1. Correlation against QT/FCA, L&amp;E, D&amp;E, and ABAC Ecosystems</p>
    <p>2. Custom data ecosystem targeting relevant class action content</p>
    <p>3. QT/FCA Ecosystem intelligence reporting</p>
  </div>

  <div class="brand">
    <span class="brand-name">Veradyn</span>
  </div>
</div>
</body>
</html>
```